Business card design for new, innovative company - BluePlinth

We are a new company looking for a business card design that is fun, different and quirky. Must use corporate colour green - CMYK C:55, M:0, Y:100, K:0, and corporate colour grey - C:0, M:0, Y: 0, K:70.

We have developed the first real time data application, in which people are able to profile the data of their existing customers in order to pull out more good fit clients to direct their marketing activities at.

Industry/Entity Type

Marketing

Requirements
Must have
• Logo, name, title, telephone number, fax number, email, website, address

```html
<!DOCTYPE html>
<html lang="en">
<head>
<meta charset="utf-8">
<title>BluePlinth Business Card</title>
<link href="https://fonts.googleapis.com/css2?family=Open+Sans:wght@400;600;700;800&display=swap" rel="stylesheet">
<style>
  :root {
    --brand-green: #76b82a;
    --brand-grey: #4d4d4d;
    --card-white: #ececec;
    --page-bg: #d9d9d6;
    --text-dark: #3a3a3a;
  }
  * { margin: 0; padding: 0; box-sizing: border-box; }
  html, body {
    width: 1200px;
    height: 900px;
    overflow: hidden;
    background: var(--page-bg);
    font-family: "Open Sans", Arial, sans-serif;
  }
  .canvas {
    width: 1200px;
    height: 900px;
    display: flex;
    flex-direction: column;
    align-items: center;
    justify-content: center;
    gap: 40px;
  }
  .card {
    position: relative;
    width: 600px;
    height: 345px;
    border-radius: 3px;
    overflow: hidden;
    box-shadow: 0 6px 18px rgba(0,0,0,0.18);
  }

  /* Front side */
  .card-front { background: var(--card-white); color: var(--text-dark); }
  .card-front .brand-name {
    position: absolute;
    top: 74px;
    left: 236px;
    display: flex;
    align-items: center;
    gap: 10px;
    font-weight: 800;
    font-size: 54px;
    letter-spacing: -2px;
    color: var(--brand-grey);
    line-height: 1;
  }
  .brand-mark {
    width: 20px;
    height: 20px;
    background: var(--brand-green);
    transform: rotate(12deg) translateY(-14px);
  }
  .name-band {
    position: absolute;
    top: 150px;
    left: 0;
    width: 100%;
    height: 48px;
    background: var(--brand-green);
    display: flex;
    align-items: center;
    padding-left: 236px;
    gap: 12px;
    color: #ffffff;
  }
  .person-name {
    font-weight: 700;
    font-size: 21px;
    letter-spacing: 0.5px;
    text-transform: uppercase;
  }
  .job-title {
    font-weight: 400;
    font-size: 14px;
    padding-left: 12px;
    border-left: 2px solid rgba(255,255,255,0.7);
  }
  .contact-list {
    position: absolute;
    left: 28px;
    top: 216px;
    list-style: none;
    font-size: 14px;
    line-height: 1.5;
  }
  .contact-list li { display: flex; align-items: center; gap: 8px; }
  .contact-list .arrow { width: 7px; height: 9px; flex: none; }
  .contact-list .spacer { width: 7px; flex: none; }
  .company-address {
    position: absolute;
    right: 28px;
    top: 216px;
    text-align: right;
    font-style: normal;
    font-size: 14px;
    line-height: 1.5;
  }
  .company-address .company { font-weight: 700; }
  .website-front {
    margin-top: 6px;
    color: var(--brand-green);
    font-weight: 600;
  }

  /* Back side */
  .card-back {
    background: var(--brand-green);
    color: #ffffff;
    display: flex;
    align-items: center;
    justify-content: center;
  }
  .back-lockup { display: flex; flex-direction: column; align-items: flex-end; }
  .card-back .brand-name {
    display: flex;
    align-items: center;
    gap: 10px;
    font-weight: 800;
    font-size: 58px;
    letter-spacing: -2px;
    line-height: 1;
  }
  .card-back .brand-mark { background: #ffffff; }
  .website { font-size: 15px; margin-top: 6px; }
</style>
</head>
<body>
<main class="canvas">
  <section class="card card-back" aria-label="Business card back">
    <div class="back-lockup">
      <div class="brand-name"><span>BluePlinth</span><span class="brand-mark"></span></div>
      <div class="website">www.blueplinth.com</div>
    </div>
  </section>

  <section class="card card-front" aria-label="Business card front">
    <div class="brand-name"><span>BluePlinth</span><span class="brand-mark"></span></div>
    <div class="name-band">
      <span class="person-name">Joanna Fairley</span>
      <span class="job-title">Marketing Director</span>
    </div>
    <ul class="contact-list">
      <li>
        <svg class="arrow" viewBox="0 0 7 9"><path d="M1 1 L5.5 4.5 L1 8" fill="none" stroke="var(--brand-green)" stroke-width="1.8"/></svg>
        079 5550 1234 (cell)
      </li>
      <li>
        <svg class="arrow" viewBox="0 0 7 9"><path d="M1 1 L5.5 4.5 L1 8" fill="none" stroke="var(--brand-green)" stroke-width="1.8"/></svg>
        013 5550 6789 (office)
      </li>
      <li>
        <svg class="arrow" viewBox="0 0 7 9"><path d="M1 1 L5.5 4.5 L1 8" fill="none" stroke="var(--brand-green)" stroke-width="1.8"/></svg>
        013 5550 6790 (fax)
      </li>
      <li><span class="spacer"></span>joanna.fairley@northfieldsupply.com</li>
    </ul>
    <address class="company-address">
      <div class="company">Northfield Marketing Solutions Limited</div>
      <div>27c Elmstead Road, Ashby</div>
      <div>Westshire, AB12 3CD</div>
      <div class="website-front">www.blueplinth.com</div>
    </address>
  </section>
</main>
</body>
</html>
```